Harborline Motors LLC

Car Dealer Customer Service
Address: 2741 Linden Avenue, Shelbyville, TN 37162
web: www.harborlinemotorstn.net
email: harborlinemotorstn@mailbox-example.net
Phone: (931) 555-0148
Phone: (629) 555-0173

```html
<!DOCTYPE html>
<html lang="en">
<head>
<meta charset="utf-8">
<title>Harborline Motors – Business Card</title>
<link href="https://fonts.googleapis.com/css2?family=Montserrat:wght@400;500;700&display=swap" rel="stylesheet">
<style>
  :root {
    --page-bg: #e3e5e4;
    --card-white: #ffffff;
    --brand-blue: #1f80bf;
    --brand-blue-deep: #1a72ad;
    --brand-yellow: #f0b83a;
    --text-white: #ffffff;
  }
  * { margin: 0; padding: 0; box-sizing: border-box; }
  html, body {
    width: 1200px; height: 800px; overflow: hidden;
    background: var(--page-bg);
    font-family: "Montserrat", sans-serif;
  }
  .canvas { position: relative; width: 1200px; height: 800px; }

  .card {
    position: absolute;
    width: 440px; height: 275px;
    background: var(--card-white);
    box-shadow: 0 2px 4px rgba(0,0,0,0.18);
    overflow: hidden;
  }
  .card--front { left: 192px; top: 101px; }
  .card--back  { left: 567px; top: 423px; }

  .card__art { position: absolute; inset: 0; width: 100%; height: 100%; }

  .front__identity { position: absolute; left: 24px; top: 62px; color: var(--text-white); }
  .front__name { font-weight: 700; font-size: 19px; letter-spacing: 0.5px; line-height: 1; }
  .front__role { font-weight: 500; font-size: 10.5px; margin-top: 5px; margin-left: 1px; }

  .front__address, .front__contacts {
    position: absolute; left: 24px; color: var(--text-white);
    font-size: 8.8px; line-height: 12.5px; font-weight: 400;
  }
  .front__address { top: 137px; }
  .front__contacts { top: 192px; }

  .brand { position: absolute; display: flex; flex-direction: column; align-items: center; }
  .brand__dot { border-radius: 50%; background: var(--brand-blue); }
  .brand__name { color: var(--brand-blue); font-weight: 700; white-space: nowrap; margin-top: 8px; }

  .brand--front { left: 290px; top: 24px; width: 140px; }
  .brand--front .brand__dot { width: 54px; height: 54px; }
  .brand--front .brand__name { font-size: 11px; }

  .brand--back { left: 0; width: 440px; top: 88px; }
  .brand--back .brand__dot { width: 80px; height: 80px; }
  .brand--back .brand__name { font-size: 19px; margin-top: 12px; }

  .back__web {
    position: absolute; left: 45px; bottom: 5px;
    color: var(--text-white); font-size: 8.5px; font-weight: 500;
  }
</style>
</head>
<body>
<main class="canvas">

  <section class="card card--front" aria-label="Business card front">
    <svg class="card__art" viewBox="0 0 440 275" aria-hidden="true">
      <defs>
        <linearGradient id="blue-panel" x1="0" y1="0" x2="0" y2="1">
          <stop offset="0" stop-color="var(--brand-blue-deep)"/>
          <stop offset="1" stop-color="var(--brand-blue)"/>
        </linearGradient>
      </defs>
      <path d="M0,0 H201 C255,0 268,70 285,140 C305,225 375,255 440,258 V275 H0 Z" fill="url(#blue-panel)"/>
      <path d="M277,134 C285,190 320,232 391,245 C330,232 292,200 277,134 Z" fill="var(--brand-yellow)" stroke="var(--brand-yellow)" stroke-width="3" stroke-linejoin="round"/>
    </svg>

    <div class="front__identity">
      <h1 class="front__name">NAME SURNAME</h1>
      <p class="front__role">Car Dealer Customer Service</p>
    </div>

    <p class="front__address">2741 Linden Avenue, Shelbyville,<br>TN 37162</p>

    <p class="front__contacts">
      (931) 555-0148<br>
      (629) 555-0173<br>
      harborlinemotorstn@mailbox-example.net<br>
      www.harborlinemotorstn.net
    </p>

    <div class="brand brand--front">
      <span class="brand__dot"></span>
      <span class="brand__name">HARBORLINE MOTORS</span>
    </div>
  </section>

  <section class="card card--back" aria-label="Business card back">
    <svg class="card__art" viewBox="0 0 440 275" aria-hidden="true">
      <path d="M0,256 H240 C255,256 262,264 270,275 H0 Z" fill="var(--brand-blue)"/>
    </svg>

    <div class="brand brand--back">
      <span class="brand__dot"></span>
      <span class="brand__name">HARBORLINE MOTORS</span>
    </div>

    <p class="back__web">www.harborlinemotorstn.net</p>
  </section>

</main>
</body>
</html>
```